Visual consulting framework

Thornwell Advisory is a financial consulting business that takes it clients on the following journey:
1. Get fit (disciplined)
2. Get funded (access to capital)
3. Get big (grow)
4. Get out (exit with wealth)
Over thirty years we have identified that the key to being successful on this journey are the following elements or components.
1. Vision
2. Strategy
3. Structure
4. Product & services
5. Sales and marketing
6. System and processes
7. People
8. Culture
9. Finance
10. M&A
11. Performance monitoring
12. Risk management
We require a visual representation of these elements and the journey to communicate to clients and prospects in marketing material.
Look and feel
Each slider illustrates characteristics of the customer's brand and the style your logo design should communicate.

```html
<!DOCTYPE html>
<html lang="en">
<head>
<meta charset="utf-8">
<title>Thornwell Advisory – Consulting Framework</title>
<link href="https://fonts.googleapis.com/css2?family=Montserrat:wght@400;500;600&display=swap" rel="stylesheet">
<style>
  :root{
    --stage:#000000;
    --paper:#f4f4f4;
    --brand-orange:#f39229;
    --brand-blue:#2aaae2;
    --headline:#1fa3dc;
    --ink:#111111;
    --axis:#1a1a1a;
    --guide:#9a9a9a;
    --top-1:#f9c08a; --top-2:#fdd05e; --top-3:#fde39b; --top-4:#f6d0d0;
    --cap-left-top:#f4a259; --cap-right-top:#efaaa3;
    --bot-1:#bf8a33; --bot-2:#fdcc5e; --bot-3:#ec8379; --bot-4:#a92628;
    --cap-left-bot:#7d5a2a; --cap-right-bot:#6f1a1a;
    --sky:#8dd3f3; --tan:#c4bba9; --stone:#e8e6e1; --white:#ffffff;
  }
  html,body{margin:0;padding:0;overflow:hidden;background:var(--stage);}
  .canvas{width:1200px;height:675px;display:block;}
  .framework text{font-family:'Montserrat',sans-serif;fill:var(--ink);}
  .label{font-size:21px;font-weight:500;text-anchor:middle;}
  .stage-label{font-size:21px;font-weight:500;text-anchor:middle;}
  .headline{font-size:43px;font-weight:500;fill:var(--headline) !important;text-anchor:middle;}
  .wordmark{font-size:30px;font-weight:400;fill:var(--brand-orange) !important;letter-spacing:1px;}
  .hero{font-size:52px;font-weight:600;letter-spacing:26px;}
  .hero-a{fill:var(--brand-orange) !important;}
  .hero-b{fill:var(--brand-blue) !important;}
  .icon{fill:var(--ink);}
  .icon-line{fill:none;stroke:var(--ink);stroke-width:5;stroke-linecap:round;stroke-linejoin:round;}
</style>
</head>
<body>
<svg class="canvas framework" viewBox="0 0 1920 1080" width="1200" height="675" xmlns="http://www.w3.org/2000/svg">
  <defs>
    <clipPath id="outer-track"><rect x="343" y="383" width="1232" height="477" rx="238.5"/></clipPath>
    <clipPath id="inner-track"><rect x="460" y="498" width="1000" height="247" rx="123.5"/></clipPath>
    <marker id="axis-head" viewBox="0 0 10 10" refX="5" refY="5" markerWidth="5" markerHeight="5" orient="auto-start-reverse">
      <path d="M0 0 L10 5 L0 10 Z" fill="#1a1a1a"/>
    </marker>
    <marker id="guide-head" viewBox="0 0 10 10" refX="5" refY="5" markerWidth="4" markerHeight="4" orient="auto">
      <path d="M0 0 L10 5 L0 10 Z" fill="#9a9a9a"/>
    </marker>
  </defs>

  <!-- backdrop -->
  <rect class="slide" x="222" y="125" width="1476" height="830" fill="var(--paper)"/>
  <rect class="band-left" x="222" y="622" width="738" height="333" fill="var(--brand-orange)"/>
  <rect class="band-right" x="960" y="622" width="738" height="333" fill="var(--brand-blue)"/>

  <!-- header -->
  <g class="brand">
    <circle cx="340" cy="215" r="30" fill="var(--brand-orange)"/>
    <text class="wordmark" x="384" y="207">THORNWELL</text>
    <text class="wordmark" x="384" y="244">ADVISORY</text>
  </g>
  <line x1="640" y1="170" x2="640" y2="266" stroke="#555" stroke-width="1.5"/>
  <text class="headline" x="1174" y="207">Our purpose is clear, we get companies</text>
  <text class="headline" x="1174" y="258">and their founders, fit, funded, big and out</text>

  <!-- outer ring: components -->
  <g class="component-ring" clip-path="url(#outer-track)">
    <rect x="343" y="383" width="194" height="239" fill="var(--cap-left-top)"/>
    <rect x="343" y="622" width="194" height="238" fill="var(--cap-left-bot)"/>
    <rect x="537" y="383" width="211" height="239" fill="var(--top-1)"/>
    <rect x="748" y="383" width="212" height="239" fill="var(--top-2)"/>
    <rect x="960" y="383" width="212" height="239" fill="var(--top-3)"/>
    <rect x="1172" y="383" width="212" height="239" fill="var(--top-4)"/>
    <rect x="1384" y="383" width="191" height="239" fill="var(--cap-right-top)"/>
    <rect x="537" y="622" width="211" height="238" fill="var(--bot-1)"/>
    <rect x="748" y="622" width="212" height="238" fill="var(--bot-2)"/>
    <rect x="960" y="622" width="212" height="238" fill="var(--bot-3)"/>
    <rect x="1172" y="622" width="212" height="238" fill="var(--bot-4)"/>
    <rect x="1384" y="622" width="191" height="238" fill="var(--cap-right-bot)"/>
  </g>

  <!-- inner ring: journey -->
  <g class="journey-ring" clip-path="url(#inner-track)">
    <rect x="460" y="498" width="288" height="124" fill="var(--sky)"/>
    <rect x="748" y="498" width="212" height="124" fill="var(--tan)"/>
    <rect x="960" y="498" width="212" height="124" fill="var(--stone)"/>
    <rect x="1172" y="498" width="288" height="124" fill="var(--white)"/>
    <rect x="460" y="622" width="288" height="123" fill="var(--white)"/>
    <rect x="748" y="622" width="212" height="123" fill="var(--stone)"/>
    <rect x="960" y="622" width="212" height="123" fill="var(--tan)"/>
    <rect x="1172" y="622" width="288" height="123" fill="var(--sky)"/>
  </g>

  <!-- axes -->
  <g class="axes" stroke="var(--axis)" stroke-width="1.5" marker-start="url(#axis-head)" marker-end="url(#axis-head)">
    <line x1="280" y1="622" x2="1640" y2="622"/>
    <line x1="537" y1="312" x2="537" y2="922"/>
    <line x1="748" y1="312" x2="748" y2="922"/>
    <line x1="960" y1="312" x2="960" y2="922"/>
    <line x1="1172" y1="312" x2="1172" y2="922"/>
    <line x1="1384" y1="312" x2="1384" y2="922"/>
  </g>

  <!-- centre pill -->
  <rect class="hero-pill" x="537" y="575" width="846" height="93" rx="46.5" fill="var(--white)" stroke="var(--axis)" stroke-width="1.5"/>
  <text class="hero" y="643"><tspan class="hero-a" x="618">MARKET</tspan><tspan class="hero-b" x="985">LEADER</tspan></text>

  <!-- guides -->
  <g class="guides" stroke="var(--guide)" stroke-width="4">
    <line x1="642" y1="575" x2="642" y2="550" marker-end="url(#guide-head)"/>
    <line x1="854" y1="575" x2="854" y2="550" marker-end="url(#guide-head)"/>
    <line x1="1066" y1="575" x2="1066" y2="550" marker-end="url(#guide-head)"/>
    <line x1="1278" y1="575" x2="1278" y2="550" marker-end="url(#guide-head)"/>
    <line x1="642" y1="670" x2="642" y2="688"/><line x1="642" y1="725" x2="642" y2="745"/>
    <line x1="854" y1="670" x2="854" y2="688"/><line x1="854" y1="725" x2="854" y2="745"/>
    <line x1="1066" y1="670" x2="1066" y2="688"/><line x1="1066" y1="725" x2="1066" y2="745"/>
    <line x1="1278" y1="670" x2="1278" y2="688"/><line x1="1278" y1="725" x2="1278" y2="745"/>
  </g>

  <!-- journey labels -->
  <text class="stage-label" x="642" y="531">Disciplined</text>
  <text class="stage-label" x="854" y="531">Access to Capital</text>
  <text class="stage-label" x="1066" y="531">Grow</text>
  <text class="stage-label" x="1278" y="531">Exit With Wealth</text>
  <text class="stage-label" x="642" y="714">Get Fit</text>
  <text class="stage-label" x="854" y="716">Get Funded</text>
  <text class="stage-label" x="1066" y="716">Get Big</text>
  <text class="stage-label" x="1278" y="716">Get Out</text>

  <!-- component labels -->
  <text class="label" x="642" y="338">Performance</text>
  <text class="label" x="642" y="364">Monitoring</text>
  <text class="label" x="854" y="351">M&amp;A</text>
  <text class="label" x="1066" y="351">Finance</text>
  <text class="label" x="1278" y="351">People</text>
  <text class="label" x="318" y="445">Risk</text>
  <text class="label" x="318" y="471">Management</text>
  <text class="label" x="1582" y="458">Culture</text>
  <text class="label" x="318" y="805">Structure</text>
  <text class="label" x="1602" y="793">Systems</text>
  <text class="label" x="1602" y="819">&amp; Process</text>
  <text class="label" x="642" y="902">Strategy</text>
  <text class="label" x="854" y="902">Vision</text>
  <text class="label" x="1066" y="889">Products &amp;</text>
  <text class="label" x="1066" y="915">Services</text>
  <text class="label" x="1278" y="889">Sales &amp;</text>
  <text class="label" x="1278" y="915">Marketing</text>

  <!-- icons -->
  <g class="icon-clipboard">
    <rect class="icon-line" x="617" y="410" width="48" height="64" rx="3"/>
    <rect class="icon" x="630" y="404" width="22" height="12" rx="3"/>
    <path class="icon-line" d="M626 436 l6 6 l10 -12 M626 456 l6 6 l10 -12"/>
  </g>
  <rect role="img" aria-label="Handshake icon" x="808" y="415" width="92" height="50" rx="25" fill="var(--ink)" opacity="0.85"/>
  <g class="icon-coins">
    <path class="icon" d="M1022 452 l38 -22 l30 14 l-38 22 Z"/>
    <ellipse class="icon" cx="1085" cy="420" rx="22" ry="8"/>
    <rect class="icon" x="1063" y="420" width="44" height="44"/>
    <path d="M1063 432 h44 M1063 444 h44 M1063 456 h44" stroke="var(--top-3)" stroke-width="3"/>
  </g>
  <rect role="img" aria-label="Team icon" x="1246" y="410" width="64" height="64" rx="14" fill="var(--ink)" opacity="0.85"/>
  <g class="icon-warning">
    <path class="icon-line" d="M421 494 L453 550 L389 550 Z"/>
    <rect class="icon" x="418" y="512" width="6" height="22"/>
    <circle class="icon" cx="421" cy="541" r="3.5"/>
  </g>
  <g class="icon-culture">
    <path class="icon" d="M1486 530 l-18 -18 a10 10 0 0 1 18 -12 a10 10 0 0 1 18 12 Z"/>
    <path class="icon-line" d="M1452 510 q-4 26 20 44 M1520 510 q4 26 -20 44"/>
  </g>
  <g class="icon-structure">
    <path class="icon-line" style="stroke-width:3" d="M408 720 h30 v20 h30 M420 745 h20 v-30 M430 760 l10 -10 h25 M455 705 v50"/>
    <circle class="icon" cx="455" cy="732" r="5"/><circle class="icon" cx="437" cy="705" r="4"/>
  </g>
  <g class="icon-systems">
    <rect class="icon" x="1453" y="708" width="8" height="8"/><rect class="icon" x="1466" y="708" width="18" height="8"/>
    <rect class="icon" x="1453" y="723" width="8" height="8"/><rect class="icon" x="1466" y="723" width="18" height="8"/>
    <rect class="icon" x="1453" y="738" width="8" height="8"/><rect class="icon" x="1466" y="738" width="18" height="8"/>
    <path class="icon-line" style="stroke-width:7" d="M1492 710 l14 34 l20 -38"/>
  </g>
  <g class="icon-pawn">
    <circle class="icon" cx="642" cy="777" r="10"/>
    <path class="icon" d="M634 790 h16 l-3 6 h-10 Z M636 798 h12 l5 26 h-22 Z"/>
    <rect class="icon" x="622" y="826" width="40" height="12" rx="3"/>
  </g>
  <g class="icon-eye">
    <path class="icon" d="M804 803 q50 -60 100 0 q-50 60 -100 0 Z"/>
    <circle cx="854" cy="803" r="21" fill="var(--bot-2)"/>
    <circle class="icon" cx="854" cy="803" r="13"/>
  </g>
  <g class="icon-products">
    <rect class="icon-line" style="stroke-width:4" x="1030" y="778" width="16" height="16"/>
    <rect class="icon-line" style="stroke-width:4" x="1058" y="778" width="16" height="16"/>
    <rect class="icon" x="1085" y="776" width="20" height="20"/>
    <rect class="icon-line" style="stroke-width:5" x="1025" y="805" width="82" height="22" rx="11"/>
    <circle class="icon" cx="1038" cy="816" r="4"/><circle class="icon" cx="1066" cy="816" r="4"/><circle class="icon" cx="1094" cy="816" r="4"/>
  </g>
  <g class="icon-trophy">
    <path class="icon" d="M1256 775 h44 v18 a22 22 0 0 1 -44 0 Z"/>
    <path class="icon-line" d="M1256 780 h-12 q0 22 18 24 M1300 780 h12 q0 22 -18 24"/>
    <rect class="icon" x="1273" y="812" width="10" height="12"/>
    <path class="icon" d="M1262 824 h32 l4 10 h-40 Z"/>
  </g>
</svg>
</body>
</html>
```